Business Card Design

We need a new business card design for a CPA office that has been in business for over 10 years. We are a Accounting Concierge firm that offers the following services: Certified Public Accountant, Personal & Business Tax Preparation, Accounting, Bookkeeping, Payroll Services, Tax Litigation Services.
Certified LedgerNest CertPartner.  We would like to see designs that use the color navy blue in the company logo with classic accent colors.  We would like the card to be on a textured high pound card stock and that is more classic and less modern in design.  The final design should communicate class and professionalism.

Reason: I gave feedback to many of the designers with some changes.  Please re-read the brief as we would like to remove the photo of the man on the card.  We also want only light grey or white background, not navy or blue - the navy or blue tones should be the font or accent colors.  Please also, consider creating a logo with the initials P&W or PW or P&W CPA.

Industry/Entity Type
Business
Contact Information for Business Card
Pellford & Company CPA, Dominic Pellford III, 4317 Larkmoor Road, Suite D, Bradenton, FL  34519, Phone: (941) 555-0137, Fax: (941) 555-0182, Email: Dominic@DPellfordCPA.example, Website: www.DPellfordCPA.example
Requirements
Must have
- LedgerNest Logo

Should not have
- we no longer want the photo on the card.

```html
<!DOCTYPE html>
<html lang="en">
<head>
<meta charset="utf-8">
<title>Pellford &amp; Company CPA — Business Card</title>
<link rel="stylesheet" href="https://fonts.googleapis.com/css2?family=Questrial&display=swap">
<style>
  :root {
    --page-bg: #e9e9e6;
    --card-white: #f7f7f5;
    --panel-grey: #e3e4e9;
    --navy: #1e2350;
    --navy-text: #2f3470;
    --seam-navy: #1e2350;
    --seam-grey: #9a9caa;
    --badge-gold: #f2b61c;
  }
  * { box-sizing: border-box; margin: 0; padding: 0; }
  html, body {
    width: 1200px; height: 1200px; overflow: hidden;
    background: var(--page-bg);
    font-family: "Questrial", "Century Gothic", sans-serif;
  }
  .business-card {
    position: absolute; left: 100px; top: 314px;
    width: 1000px; height: 572px;
    background: var(--card-white);
    overflow: hidden;
    box-shadow: 0 10px 30px rgba(0,0,0,0.18);
  }
  .card-shapes { position: absolute; inset: 0; }
  .company-name {
    position: absolute; left: 62px; top: 78px;
    font-size: 56px; line-height: 1.12; font-weight: 400;
    color: var(--navy-text); letter-spacing: 0.5px;
  }
  .partner-badge {
    position: absolute; left: 115px; top: 400px;
    width: 170px; height: 124px;
    border-radius: 50%;
    background: var(--badge-gold);
  }
  .holder-name {
    position: absolute; right: 56px; top: 42px;
    font-size: 42px; color: var(--navy); font-weight: 400;
    letter-spacing: 0.5px;
  }
  .contact-list {
    position: absolute; left: 490px; top: 140px;
    list-style: none; color: var(--navy-text);
    font-size: 27px; line-height: 1.22;
  }
  .contact-item { display: flex; align-items: flex-start; margin-bottom: 18px; }
  .contact-icon { width: 24px; height: 24px; margin: 4px 18px 0 0; flex: none; fill: var(--navy); }
</style>
</head>
<body>
  <article class="business-card">
    <svg class="card-shapes" viewBox="0 0 1000 572" preserveAspectRatio="none" aria-hidden="true">
      <path d="M374 0 Q482 280 394 572 L1000 572 L1000 0 Z" fill="var(--panel-grey)"/>
      <path d="M362 0 Q470 280 382 572 L388 572 Q476 280 368 0 Z" fill="var(--seam-grey)"/>
      <path d="M368 0 Q476 280 388 572 L396 572 Q484 280 376 0 Z" fill="var(--seam-navy)"/>
    </svg>

    <h1 class="company-name">Pellford &amp;<br>Company<br>CPA, LLC</h1>
    <div class="partner-badge" role="img" aria-label="LedgerNest CertPartner certification badge"></div>

    <h2 class="holder-name">Dominic Pellford</h2>

    <ul class="contact-list">
      <li class="contact-item">
        <svg class="contact-icon" viewBox="0 0 24 24"><path d="M12 1a8 8 0 0 0-8 8c0 6 8 14 8 14s8-8 8-14a8 8 0 0 0-8-8zm0 11a3 3 0 1 1 0-6 3 3 0 0 1 0 6z"/></svg>
        <span>III, 4317 Larkmoor Road, Suite D,<br>Bradenton, FL 34519</span>
      </li>
      <li class="contact-item">
        <svg class="contact-icon" viewBox="0 0 24 24"><path d="M6.6 10.8a15 15 0 0 0 6.6 6.6l2.2-2.2c.3-.3.7-.4 1-.2 1.1.4 2.3.6 3.6.6.6 0 1 .4 1 1V20c0 .6-.4 1-1 1C10.6 21 3 13.4 3 4c0-.6.4-1 1-1h3.5c.6 0 1 .4 1 1 0 1.3.2 2.5.6 3.6.1.3 0 .7-.2 1z"/></svg>
        <span>(941) 555-0137</span>
      </li>
      <li class="contact-item">
        <svg class="contact-icon" viewBox="0 0 24 24"><path d="M6 3h9l3 3v4H6zM3 11h18v9H3zm3 2v2h4v-2z"/></svg>
        <span>(941) 555-0182</span>
      </li>
      <li class="contact-item">
        <svg class="contact-icon" viewBox="0 0 24 24"><path d="M2 5h20v14H2zm2 2v.5l8 5.5 8-5.5V7zm0 3v7h16v-7l-8 5.5z"/></svg>
        <span>dominic@dpellfordcpa.example</span>
      </li>
      <li class="contact-item">
        <svg class="contact-icon" viewBox="0 0 24 24"><path d="M12 2a10 10 0 1 0 0 20 10 10 0 0 0 0-20zm6.9 9h-3a15 15 0 0 0-1.3-6A8 8 0 0 1 18.9 11zM12 4c.9 1.2 1.7 3.6 1.9 7h-3.8c.2-3.4 1-5.8 1.900-7zM9.4 5a15 15 0 0 0-1.3 6h-3A8 8 0 0 1 9.4 5zM5.1 13h3a15 15 0 0 0 1.3 6A8 8 0 0 1 5.1 13zM12 20c-.9-1.2-1.7-3.6-1.9-7h3.8c-.2 3.4-1 5.8-1.9 7zm2.6-1a15 15 0 0 0 1.3-6h3a8 8 0 0 1-4.3 6z"/></svg>
        <span>www.dpellfordcpa.example</span>
      </li>
    </ul>
  </article>
</body>
</html>
```